Business Card Design Project

This is the first time we use our new logo. We need a business card that we can use both on our institutional corporate relationships and also that works for our staff that deals with consumers directly.

VELUNDA is a new company dedicated to empower consumers and to provide them with the best choices for specialized health care using the latest telemedicine technology (medicine at a distance via videoconference).

We want to print this cards in high quality materials and process. We will like designs that allow us to use UV spot varnish and other techniques that will differentiate us.

We are including Two different versions of Color logos. In addition we are including white over black background logos. Those can be used replacing the black for a color.

Please note this is the first time we will be creating any corporate materials with our new logo and colors.

Target Market(s)

34+ consumers of medium high and high socioeconomic levels.

Industry/Entity Type

Health

Requirements
Must have
• Our logo on its original colors
Should not have
• Any other graphical element or design that is not our logo

```html
<!DOCTYPE html>
<html lang="en">
<head>
<meta charset="utf-8">
<title>VELUNDA Business Card</title>
<link rel="stylesheet" href="https://fonts.googleapis.com/css2?family=Arimo:wght@400;700&display=swap">
<style>
  :root {
    --stage: #888686;
    --card: #ffffff;
    --brand-navy: #0d3a5c;
    --brand-teal: #0f4d6e;
    --ink-grey: #6b6b6b;
    --rule-grey: #555555;
  }
  * { margin: 0; padding: 0; box-sizing: border-box; }
  html, body {
    width: 1200px;
    height: 848px;
    overflow: hidden;
    background: var(--stage);
    font-family: "Arimo", Arial, sans-serif;
  }
  .canvas {
    position: relative;
    width: 1200px;
    height: 848px;
  }
  .card {
    position: absolute;
    width: 729px;
    height: 316px;
    background: var(--card);
    border-radius: 2px;
  }
  /* Front side */
  .card--front { left: 40px; top: 60px; }
  .front-brand {
    position: absolute;
    left: 170px;
    top: 118px;
    display: flex;
    align-items: center;
    gap: 22px;
  }
  .front-brand__dot {
    width: 64px;
    height: 64px;
    border-radius: 50%;
    background: var(--brand-navy);
  }
  .front-brand__name {
    font-size: 58px;
    font-weight: 700;
    letter-spacing: 5px;
    color: var(--brand-navy);
  }
  /* Back side */
  .card--back { left: 336px; top: 469px; }
  .back-company {
    position: absolute;
    left: 0;
    width: 258px;
    top: 72px;
    text-align: center;
    font-size: 20px;
    font-weight: 700;
    color: var(--brand-teal);
  }
  .back-role {
    position: absolute;
    left: 0;
    width: 258px;
    top: 116px;
    text-align: center;
    font-size: 18px;
    font-weight: 700;
    color: var(--ink-grey);
  }
  .back-divider {
    position: absolute;
    left: 256px;
    top: 59px;
    width: 3px;
    height: 200px;
    background: var(--rule-grey);
    border-radius: 2px;
  }
  .back-person {
    position: absolute;
    left: 301px;
    top: 122px;
    font-size: 16px;
    font-weight: 700;
    color: var(--ink-grey);
  }
  .back-phone {
    position: absolute;
    left: 301px;
    top: 159px;
    font-size: 16px;
    font-weight: 700;
    color: var(--ink-grey);
    word-spacing: 8px;
  }
  .back-address {
    position: absolute;
    left: 40px;
    top: 295px;
    font-size: 13px;
    font-weight: 700;
    color: var(--ink-grey);
    white-space: nowrap;
  }
</style>
</head>
<body>
<main class="canvas">
  <section class="card card--front" aria-label="Card front">
    <div class="front-brand">
      <span class="front-brand__dot"></span>
      <span class="front-brand__name">VELUNDA</span>
    </div>
  </section>

  <section class="card card--back" aria-label="Card back">
    <p class="back-company">VELUNDA</p>
    <p class="back-role">Marketing Manager</p>
    <span class="back-divider"></span>
    <p class="back-person">MR.TOMAS ARLEN</p>
    <p class="back-phone">XX XXXXX XXXXXX</p>
    <p class="back-address">xxxx xxxx,&nbsp; xxxxxxxxxxxxxxx , xxxxx, xxxxxxxxxxx, xxxxxxxxxxxxxxxxxx..</p>
  </section>
</main>
</body>
</html>
```